Brochure & Business card design

Looking for a new business card design i want it to be modern and sharp looking i usually order plastic business cards, and i would like to make the colors like the logo teal/charcoal i will like to have our services on icons with words.... our services are
ROOFING GUTTERS PAINTING PRESSURE WASHING EXTERIOR DESIGN & ATTIC VENTILATION. I also want to add my credentials

Target Market(s)

Oregon local market

Industry/Entity Type

Residential Construction

Contact Information for Business Card

Business info, services, number, website

Font styles to use
Serif
Sans Serif

Colors
33b8a4
5c5c5c
ffffff

Requirements
Must have
• Dale Finch
• Cell:
• Office:
• Email:
• Website:
• also i need our social media icons
• Services ROOFING GUTTERS PAINTING PRESSURE WASHING EXTERIOR DESIGN & ATTIC VENTILATION
• -icons for number, web, email, cell
• OR #584312
• Wa #KTRABLD461X7
Nice to have
• -Clean design Front & Back
• -Icons
• -shape House just like logo design
• -First Impression
Should not have
• Not Busy or lost of eye contact

```html
<!DOCTYPE html>
<html lang="en">
<head>
<meta charset="utf-8">
<title>Ridgeline Home Exteriors – Business Card</title>
<link rel="stylesheet" href="https://fonts.googleapis.com/css2?family=Barlow+Condensed:wght@400;700&family=Barlow+Semi+Condensed:wght@400&display=swap">
<style>
  :root {
    --charcoal: #5b5b5d;
    --teal: #21958a;
    --white: #ffffff;
    --page: #ffffff;
    --badge-light: #e9e9e9;
    --badge-dark: #4a4a4c;
  }
  * { box-sizing: border-box; margin: 0; padding: 0; }
  html, body { width: 1200px; height: 1000px; overflow: hidden; background: var(--page); }
  .canvas { position: relative; width: 1200px; height: 1000px; }

  .card-front {
    position: absolute; left: 271px; top: 80px; width: 659px; height: 404px;
    background: var(--charcoal);
    display: flex; align-items: center; justify-content: center;
  }
  .brand-name {
    font-family: "Barlow Condensed", sans-serif; font-weight: 700;
    color: var(--white); text-align: center; font-size: 44px; line-height: 1.05;
    letter-spacing: 1px;
  }

  .card-back {
    position: absolute; left: 271px; top: 519px; width: 656px; height: 400px;
    background: var(--charcoal);
  }
  .contact-side { position: absolute; left: 0; top: 0; width: 399px; height: 400px; }
  .person-name {
    position: absolute; left: 71px; top: 50px;
    font-family: "Barlow Condensed", sans-serif; font-weight: 700;
    font-size: 38px; color: var(--white); letter-spacing: 0.5px;
  }
  .contact-row { position: absolute; left: 0; height: 37px; display: flex; align-items: center; }
  .contact-pill {
    width: 119px; height: 37px; background: var(--teal);
    border-radius: 0 19px 19px 0;
    display: flex; align-items: center; justify-content: flex-end; padding-right: 18px;
  }
  .contact-pill svg { width: 24px; height: 24px; }
  .contact-text {
    margin-left: 11px;
    font-family: "Barlow Semi Condensed", sans-serif; font-size: 17px; color: var(--white);
  }

  .services-side {
    position: absolute; left: 399px; top: 0; width: 257px; height: 400px;
    background: var(--teal);
  }
  .service-list { position: absolute; right: 41px; top: 29px; list-style: none; }
  .service-item {
    display: flex; align-items: center; justify-content: flex-end;
    height: 36px;
    font-family: "Barlow Condensed", sans-serif; font-size: 20px; color: var(--white);
  }
  .service-icon { width: 18px; height: 18px; margin-left: 11px; }
  .badge { position: absolute; }
  .badge-cert { left: 80px; top: 303px; width: 87px; height: 32px; background: var(--badge-light); border-radius: 2px; }
  .badge-accredit { left: 175px; top: 269px; width: 40px; height: 66px; background: var(--badge-dark); border: 2px solid var(--white); border-radius: 4px; }
  .licenses {
    position: absolute; left: 0; width: 100%; top: 346px; text-align: center;
    font-family: "Barlow Condensed", sans-serif; font-size: 13px; color: var(--white);
  }
</style>
</head>
<body>
<div class="canvas">

  <section class="card-front">
    <div class="brand-name">RIDGELINE<br>HOME EXTERIORS</div>
  </section>

  <section class="card-back">
    <div class="contact-side">
      <h1 class="person-name">DALE FINCH</h1>

      <div class="contact-row" style="top:173px">
        <div class="contact-pill">
          <svg viewBox="0 0 24 24"><path fill="#fff" d="M6.6 10.8a15.1 15.1 0 0 0 6.6 6.6l2.2-2.2c.3-.3.7-.4 1-.2 1.1.4 2.3.6 3.6.6.6 0 1 .4 1 1V20c0 .6-.4 1-1 1A17 17 0 0 1 3 4c0-.6.4-1 1-1h3.5c.6 0 1 .4 1 1 0 1.3.2 2.5.6 3.6.1.3 0 .7-.2 1z"/></svg>
        </div>
        <span class="contact-text">555 718 406 &nbsp;|&nbsp; Office:</span>
      </div>

      <div class="contact-row" style="top:226px">
        <div class="contact-pill">
          <svg viewBox="0 0 24 24"><rect x="2" y="5" width="20" height="14" fill="none" stroke="#fff" stroke-width="1.8"/><path d="M2 5l10 8 10-8M2 19l7.5-7M22 19l-7.5-7" fill="none" stroke="#fff" stroke-width="1.8"/></svg>
        </div>
        <span class="contact-text">dale@ridgelinehomeext.com</span>
      </div>

      <div class="contact-row" style="top:280px">
        <div class="contact-pill">
          <svg viewBox="0 0 24 24"><circle cx="11" cy="11" r="8.5" fill="none" stroke="#fff" stroke-width="1.8"/><path d="M2.5 11h17M11 2.5c-3 3-3 14 0 17M11 2.5c3 3 3 14 0 17" fill="none" stroke="#fff" stroke-width="1.5"/><path d="M14 13l7 3-3 1 2 3-1.5 1-2-3-2 2z" fill="#fff" stroke="#21958a" stroke-width="1"/></svg>
        </div>
        <span class="contact-text">www.ridgelinehomeext.com</span>
      </div>

      <div class="contact-row" style="top:333px">
        <div class="contact-pill">
          <svg viewBox="0 0 24 24"><circle cx="12" cy="12" r="8" fill="#fff"/></svg>
        </div>
        <span class="contact-text">social: @ridgelinehomeext</span>
      </div>
    </div>

    <div class="services-side">
      <ul class="service-list">
        <li class="service-item">ROOFING<svg class="service-icon" viewBox="0 0 18 18"><path fill="#fff" d="M0 0h8v8H0zM10 0h8v8h-8zM0 10h8v8H0zM10 10h8v8h-8z"/></svg></li>
        <li class="service-item">GUTTERS<svg class="service-icon" viewBox="0 0 18 18"><path fill="#fff" d="M0 0h8v8H0zM10 0h8v8h-8zM0 10h8v8H0zM10 10h8v8h-8z"/></svg></li>
        <li class="service-item">PAINTING<svg class="service-icon" viewBox="0 0 18 18"><path fill="#fff" d="M0 0h8v8H0zM10 0h8v8h-8zM0 10h8v8H0zM10 10h8v8h-8z"/></svg></li>
        <li class="service-item">EXTERIOR DESIGN<svg class="service-icon" viewBox="0 0 18 18"><path fill="#fff" d="M0 0h8v8H0zM10 0h8v8h-8zM0 10h8v8H0zM10 10h8v8h-8z"/></svg></li>
        <li class="service-item">ATTIC VENTILATION<svg class="service-icon" viewBox="0 0 18 18"><path fill="#fff" d="M0 0h8v8H0zM10 0h8v8h-8zM0 10h8v8H0zM10 10h8v8h-8z"/></svg></li>
        <li class="service-item">PRESSURE WASHING<svg class="service-icon" viewBox="0 0 18 18"><path fill="#fff" d="M0 0h8v8H0zM10 0h8v8h-8zM0 10h8v8H0zM10 10h8v8h-8z"/></svg></li>
      </ul>
      <div class="badge badge-cert" role="img" aria-label="Roofing contractor certification badge"></div>
      <div class="badge badge-accredit" role="img" aria-label="Business accreditation badge"></div>
      <p class="licenses">OR #584312 | Wa #KTRABLD461X7</p>
    </div>
  </section>

</div>
</body>
</html>
```